Start Up sucht Sticker-, Postkarten- und Herz-Design für Gastgeschenk Seedballs für Hochzeiten
Zielgruppe
Hallo! Wir sind ein Start Up aus dem Saatgutbereich mit verschiedenen Marken. Für unser neues Produkt:
Seedballs in 50er und 100er Abpackungen für Hochzeiten (Gastgeschenke) suchen wir 3 Designs: Zum einen ein Design für den herzförmigen Anhänger (die an die Seedballs in kleinen Organzasäckchen gehangen werden), eine Postkarte die den zu Trauenden einen wunderschönen Tag wünscht und den Sticker der außen auf die Kraftkartonverpackung geklebt wird. Falls die Produkte gut angenommen werden, werden wir eine komplette Faltkartonverpackung erstellen und einsetzen.
Aufgabenstellung
Wir haben für die Marke 'Wiesenfunke' bereits ein Logo und einige Verpackungen designt. Siehe Anhang. Aber es soll hier vor allem um den Zweck der Gastgeschenke gehen mit Hauptdesign 'Hochzeit'. Logo, Organzasäckchen, Vorlage Herz anbei.
Es solls ich vor allem um das Thema 'Hochzeit' drehen, weniger um die Marke an sich. Das genutzte Papier soll weiß sein, da dies mit den meisten Hochzeitsvorlagen und Dekos zusammen passt.
Als vielleicht passende Fonts kommen: Brittany, Monterchi Serif oder andere in Frage.
Enthalten sind bei den beiden Sets
50er:
50 Seedballs in Kraftpapiertüte mit Sticker
50 Organzasäckchen
50 herzförmige Geschenkanhänger
1x Postkarte für das Ehepaar
100er
100 Seedballs in Kraftpapiertüte mit Sticker
100 Organzasäckchen
100 herzförmige Geschenkanhänger
Folgende Formate sollen genutzt werden:
Postkarte: DIN A6
Herzförmiger Geschenkanhänger: 5x5cm
Sticker für die Verpackung:
50x Seedballs: 8x18cm
100x Seedballs: 10x20cm
Ideen:
Postkarte:
Es soll nur eine allgemeine Postkarte sein die den Trauenden einen wunderschönen Tag und eine wunderschöne Ehe wünscht. Die Rückseite kann ebenfalls designed werden.
Herzförmiger Geschenkanhänger für die Organzasäckchen mit Seedball:
Dort soll etwas wie 'Lasst unsere Liebe wachsen' oder ähnliches stehen, allgemein gehalten. Die Rückseite soll eine ganz kleine Anleitung wie die Seedballs funktionieren enthalten. Siehe Design was es schon gibt.
Das Design soll sich vor allem um Hochzeit und das Thema Gastgeschenk drehen. Außen soll die Anzahl der befindlichen Seedballs stehen (50 bzw. 100) + EAN Code + unsere Kontaktdaten. EAN Codes und Daten werden von uns gestellt. Nutzt bitte zu erst einfache Platzhalter.
Wenn weitere Infos benötigt werden, dann gerne melden. Wir freuen uns auf eure Vorschläge.

```html
<!DOCTYPE html>
<html lang="de">
<head>
<meta charset="utf-8">
<title>Postkarte – Hochzeitstag</title>
<link href="https://fonts.googleapis.com/css2?family=Bodoni+Moda:wght@500&display=swap" rel="stylesheet">
<style>
  :root {
    --page-bg: #e8e8e8;
    --card-bg: #ffffff;
    --ink: #363130;
    --leaf-deep: #7f9a6a;
    --leaf-soft: #c9d8b8;
    --leaf-pale: #e6eddc;
    --blush: #ead7e6;
  }
  html, body {
    margin: 0;
    width: 1200px;
    height: 1200px;
    overflow: hidden;
    background: var(--page-bg);
  }
  .postcard {
    position: absolute;
    left: 60px;
    top: 213px;
    width: 1080px;
    height: 772px;
    background: var(--card-bg);
    overflow: hidden;
  }
  .wreath-art {
    position: absolute;
    inset: 0;
    width: 100%;
    height: 100%;
  }
  .greeting-disc {
    position: absolute;
    left: 302px;
    top: 154px;
    width: 456px;
    height: 456px;
    border-radius: 50%;
    background: var(--card-bg);
    display: flex;
    flex-direction: column;
    align-items: center;
    font-family: "Bodoni Moda", "Didot", serif;
    color: var(--ink);
  }
  .brand {
    margin-top: 52px;
    display: flex;
    flex-direction: column;
    align-items: center;
    gap: 8px;
  }
  .brand-dot {
    width: 56px;
    height: 56px;
    border-radius: 50%;
    border: 3px solid #5a4336;
    box-sizing: border-box;
  }
  .brand-name {
    font-size: 17px;
    font-weight: 500;
    color: #4a3a33;
  }
  .greeting {
    margin: 26px 0 0;
    font-size: 45px;
    font-weight: 500;
    line-height: 65px;
    text-align: center;
    letter-spacing: 0.3px;
  }
</style>
</head>
<body>
  <div class="postcard">
    <svg class="wreath-art" viewBox="0 0 1080 772" role="img" aria-label="Aquarell-Kranz aus grünen Blättern und Zweigen mit zartrosa Farbflecken rund um die Mitte der Karte">
      <defs>
        <radialGradient id="wreath-tone" cx="50%" cy="50%" r="55%">
          <stop offset="40%" stop-color="var(--leaf-soft)" />
          <stop offset="62%" stop-color="var(--leaf-deep)" stop-opacity="0.55" />
          <stop offset="82%" stop-color="var(--leaf-pale)" stop-opacity="0.6" />
          <stop offset="100%" stop-color="#ffffff" stop-opacity="0" />
        </radialGradient>
        <radialGradient id="blush-tone" cx="50%" cy="50%" r="50%">
          <stop offset="0%" stop-color="var(--blush)" />
          <stop offset="100%" stop-color="var(--blush)" stop-opacity="0" />
        </radialGradient>
      </defs>
      <ellipse cx="530" cy="400" rx="440" ry="420" fill="url(#wreath-tone)" />
      <ellipse cx="780" cy="260" rx="120" ry="110" fill="url(#blush-tone)" />
      <ellipse cx="300" cy="470" rx="110" ry="130" fill="url(#blush-tone)" />
    </svg>
    <div class="greeting-disc">
      <div class="brand">
        <span class="brand-dot"></span>
        <span class="brand-name">Wiesenfunke</span>
      </div>
      <p class="greeting">Wünscht einen<br>wunderschönen<br>Hochzeitstag!</p>
    </div>
  </div>
</body>
</html>
```